Packing Design: SNACK FOOD BAG

We are manufactures and our main product is a kind of shell-shaped corn puff in ketchup flavor: brand name is Zorbi. (See photo Red Zorbi Flips Ketchup)

We will launch 15 new products (like chips, tortilla, popcorn, biscuits, etc.) under the same logo Zorbi.
As new Products are different, their layout must be different or with different designs.
But they must all be connected together with any feature, to be easily recognized / identified as same Zorbi range of products.
-

THE MAIN PURPOSE OF THIS PROJECT CONTEST IS:

Choosing the best connection between “Red Zorbi flips ketchup" label and new designs for new products.
Customers must easily understand that new products are done from same Zorbi Factory and are part of the same Zorbi brand (production). We want new labels to naturally derive from old Zorbi design with a modern and hip connection.

We would prefer drafts where 1 part is in red color (including Zorbi Logo) and the rest of layout to be used for different designs (for different products). At the end of all different designs, they may have in common a part of their layouts, derived from Red Zorbi Ketchup.
But we warmly welcome your different ideas and different suggestions.

-
Send sample draft for any from products below:
PEANUT BUTTER CORN bag size: High 210 mm x Width 145 mm
TORTILLA CHIPS ( flavors: Nachos / Spicy Ketchup) bag size: High 160 mm x Width 130 mm
CRUNCHY CROUTONS bag size: High 160 mm x Width 115 mm
CARAMEL CORN bag size: High 210 mm x Width 145 mm

Bags are (no transparent) BOPP material, with different sizes, containing small quantities from 20 – 50 grams.
-
Details for this project can be downloaded clicking to the link below:
http://www.filmavrek.com/file/q4t7w2 and
http://www.filmavrek.com/file/m8z3k5
Updates

Reason: there are designers submitting designs at the last moments. there is no time to review and give feedback to all. apologies for any inconvenience caused to the designers who submitted earlier warm regards

Target Market(s)

Target customers are young people: children, teens, students.

Industry/Entity Type

Factory

Requirements
Must have
• The new designs must include SAME Zorbi Logo, few pieces of the product view with flavor images and FEATURES CONNECTING ALL DESIGNS TOGETHER.
Nice to have
• A Feature is needed, to connect all new products with "Zorbi flips ketchup" design and all designs together.
Connections could be any details like:
RED COLORED ribbons, RED COLORED dotted /spotted layout,
RED COLORED background containing lines within itself,
different nuances of Zorbi Logo,
or else, or else, etc.
Show us what inspires you...

We would like to see strong deep colors, with 3D or fading reflections within them.
Final designs should bring the sense of appetite (making your mouth wet).
Should not have
• - Zorbi-Logo must be used without the word 'Flips"
- Must no have connection with ZORBI carton character.
- we don't like that all products to be in all-in-red bags.

```html
<!DOCTYPE html>
<html lang="en">
<head>
<meta charset="utf-8">
<title>Zorbi snack bag labels</title>
<link rel="stylesheet" href="https://fonts.googleapis.com/css2?family=Cabin:wght@400;700&family=Cabin+Sketch:wght@400;700&display=swap">
<style>
  :root {
    --page: #e6e7ea;
    --red: #cf2129;
    --red-dark: #a8171f;
    --green: #3f6a32;
    --green-deep: #2a4a21;
    --green-light: #6f9a52;
    --yellow: #f2bd24;
    --yellow-deep: #e8a812;
    --yellow-light: #fbdc6a;
    --ink: #151515;
    --chalk: #f4f4f0;
    --band-dark: #262626;
    --note: rgba(255,255,255,.75);
  }
  * { box-sizing: border-box; margin: 0; padding: 0; }
  html, body { width: 1200px; height: 900px; overflow: hidden; }
  body {
    background: var(--page);
    font-family: "Cabin", sans-serif;
    display: flex; align-items: center; justify-content: center; gap: 64px;
  }
  .bag-label {
    position: relative; width: 414px; height: 600px; overflow: hidden;
    box-shadow: 0 4px 18px rgba(0,0,0,.12);
  }
  .bag-label--croutons {
    background: radial-gradient(ellipse at 50% 60%, var(--green-light) 0%, var(--green) 45%, var(--green-deep) 100%);
  }
  .bag-label--tortilla {
    background: radial-gradient(ellipse at 50% 55%, var(--yellow-light) 0%, var(--yellow) 50%, var(--yellow-deep) 100%);
  }
  .top-strip { position: absolute; top: 0; left: 0; right: 0; height: 16px; background: var(--red); }
  .brand-ribbon {
    position: absolute; top: 0; left: 20%; width: 60%; height: 222px;
    background: linear-gradient(90deg, var(--red-dark) 0 13%, var(--red) 13% 87%, var(--red-dark) 87%);
  }
  .ribbon-edge { position: absolute; top: 220px; left: 20%; width: 60%; height: 14px; }
  .brand-name {
    position: absolute; top: 128px; left: 0; right: 0; text-align: center;
    font-family: "Cabin", sans-serif; font-weight: 700; font-size: 96px; line-height: 1;
    color: var(--ink);
  }
  .product-visual {
    position: absolute; left: 24%; top: 272px; width: 54%; height: 146px; border-radius: 45%;
  }
  .bag-label--croutons .product-visual { background: radial-gradient(ellipse, #e9a050 0%, #d17a32 50%, rgba(209,122,50,0) 72%); }
  .bag-label--tortilla .product-visual { background: radial-gradient(ellipse, #f5c860 0%, #e39a30 50%, rgba(227,154,48,0) 72%); }
  .product-title {
    position: absolute; left: 0; right: 0; text-align: center; color: var(--chalk); line-height: 1.05;
    font-family: "Cabin Sketch", cursive; font-weight: 700;
  }
  .product-title span { display: block; }
  .bag-label--croutons .product-title {
    top: 418px; height: 82px; padding-top: 8px;
    background: linear-gradient(90deg, transparent, rgba(0,0,0,.2) 20%, rgba(0,0,0,.2) 80%, transparent);
  }
  .bag-label--croutons .title-small { font-size: 30px; }
  .bag-label--croutons .title-large { font-size: 42px; }
  .bag-label--tortilla .product-title {
    top: 430px; left: 8%; right: 8%; height: 66px; padding-top: 6px; background: var(--band-dark);
  }
  .bag-label--tortilla .title-small { font-size: 26px; }
  .bag-label--tortilla .title-large { font-size: 36px; }
  .net-weight {
    position: absolute; left: 6%; top: 498px; width: 60px; height: 40px; border-radius: 50%;
    background: var(--ink); color: var(--chalk); font-size: 15px; font-weight: 700;
    display: flex; align-items: center; justify-content: center;
  }
  .bottom-line { position: absolute; left: 0; right: 0; top: 572px; height: 5px; background: rgba(0,0,0,.55); }
  .bottom-strip { position: absolute; left: 0; right: 0; bottom: 0; height: 20px; background: var(--red); }
  .side-note {
    position: absolute; font-size: 12px; line-height: 1.1; color: var(--note); text-align: left;
  }
  .side-note--open { left: 6%; top: 76px; }
  .side-note--new { right: 4%; top: 226px; }
  .side-note--taste { left: 6%; top: 384px; transform: rotate(-20deg); }
  .bag-label--tortilla .side-note--taste { left: 5%; top: 384px; }
  .note-arrow { position: absolute; stroke: var(--note); fill: none; stroke-width: 1.4; }
</style>
</head>
<body>
  <section class="bag-label bag-label--croutons">
    <div class="top-strip"></div>
    <div class="brand-ribbon"></div>
    <svg class="ribbon-edge" viewBox="0 0 248 14" preserveAspectRatio="none">
      <polygon fill="#cf2129" points="0,0 248,0 248,4 240,14 232,4 224,14 216,4 208,14 200,4 192,14 184,4 176,14 168,4 160,14 152,4 144,14 136,4 128,14 120,4 112,14 104,4 96,14 88,4 80,14 72,4 64,14 56,4 48,14 40,4 32,14 24,4 16,14 8,4 0,14"/>
    </svg>
    <p class="side-note side-note--open">OPEN<br>HERE</p>
    <svg class="note-arrow" style="left:40px;top:30px" width="30" height="44"><path d="M10 42 C2 28 8 12 24 4 M24 4 l-8 1 M24 4 l-2 8"/></svg>
    <p class="side-note side-note--new">NEW<br>PRODUCT</p>
    <svg class="note-arrow" style="right:18px;top:258px" width="40" height="48"><path d="M30 2 C38 22 30 38 6 44 M6 44 l8 -6 M6 44 l9 3"/></svg>
    <h1 class="brand-name">Zorbi</h1>
    <div class="product-visual" role="img" aria-label="Photo of golden seasoned croutons with a basil leaf"></div>
    <p class="side-note side-note--taste">GREAT<br>TASTE</p>
    <h2 class="product-title"><span class="title-small">CRUNCHY</span><span class="title-large">CROUTONS</span></h2>
    <div class="net-weight">20gr.</div>
    <div class="bottom-line"></div>
    <div class="bottom-strip"></div>
  </section>

  <section class="bag-label bag-label--tortilla">
    <div class="top-strip"></div>
    <div class="brand-ribbon"></div>
    <svg class="ribbon-edge" viewBox="0 0 248 14" preserveAspectRatio="none">
      <polygon fill="#cf2129" points="0,0 248,0 248,4 240,14 232,4 224,14 216,4 208,14 200,4 192,14 184,4 176,14 168,4 160,14 152,4 144,14 136,4 128,14 120,4 112,14 104,4 96,14 88,4 80,14 72,4 64,14 56,4 48,14 40,4 32,14 24,4 16,14 8,4 0,14"/>
    </svg>
    <p class="side-note side-note--open">OPEN<br>HERE</p>
    <svg class="note-arrow" style="left:40px;top:30px" width="30" height="44"><path d="M10 42 C2 28 8 12 24 4 M24 4 l-8 1 M24 4 l-2 8"/></svg>
    <p class="side-note side-note--new">NEW<br>PRODUCT</p>
    <svg class="note-arrow" style="right:18px;top:258px" width="40" height="48"><path d="M30 2 C38 22 30 38 6 44 M6 44 l8 -6 M6 44 l9 3"/></svg>
    <h1 class="brand-name">Zorbi</h1>
    <div class="product-visual" role="img" aria-label="Photo of cheese flavored tortilla chips"></div>
    <p class="side-note side-note--taste">CHEESE<br>FLAVORED</p>
    <h2 class="product-title"><span class="title-small">TASTY</span><span class="title-large">TORTILLA</span></h2>
    <div class="net-weight">20gr.</div>
    <div class="bottom-line"></div>
    <div class="bottom-strip"></div>
  </section>
</body>
</html>
```